Contemporary Elegant Business Card Design for an International Trade Company in the Wine Industry

We need a new business card design for an international trade company in the wine and winemaking industry. The overall feel of the card should be contemporary, upscale, luxurious and elegant. It should communicate confidence and professionalism. The colors should complementary to our logo design (burgundy, gold, and black).
Inspiration: rich velvet tapestry
The card should include the following information:
Business: Brovenna Trading/Shipping, LLC.
Name: Marcus T. Hollenbrand
Title: CEO
Email: mark@brovennatrading.example
Phone: 555-294-6172
www.brovennatrading.example
Updates
Project Deadline Extended
Reason: We'd like the designers that we requested some additional designs from to still submit designs. Thank you!
Industry/Entity Type
Business
Contact Information for Business Card
Title: CEO
Phone: 555-294-6172
www.brovennatrading.example
Look and feel

```html
<!DOCTYPE html>
<html lang="en">
<head>
<meta charset="utf-8">
<title>Brovenna Trading/Shipping – Business Card</title>
<link rel="stylesheet" href="https://fonts.googleapis.com/css2?family=Open+Sans:wght@400;600&display=swap">
<style>
  :root {
    --burgundy: #6e111d;
    --gold: #dca742;
    --tapestry-dark: #4a3d22;
    --tapestry-mid: #7a6636;
    --tapestry-light: #9c8444;
    --ink: #3a3a3a;
    --paper: #ffffff;
  }
  * { box-sizing: border-box; margin: 0; padding: 0; }
  html, body {
    width: 1200px; height: 329px; overflow: hidden;
    background: var(--paper);
    font-family: "Open Sans", Arial, sans-serif;
  }
  .sheet { position: relative; width: 1200px; height: 329px; overflow: hidden; }

  .card { position: absolute; top: 0; width: 550px; height: 329px; overflow: hidden; }
  .card--back { left: 0; }
  .card--front { left: 650px; background: var(--paper); }

  .card__art { position: absolute; inset: 0; width: 550px; height: 329px; }

  .tapestry-fill { fill: url(#tapestry); }

  .brand-mark {
    position: absolute; width: 88px;
    display: flex; flex-direction: column; align-items: center; gap: 6px;
  }
  .brand-mark__square { width: 70px; height: 70px; background: var(--burgundy); }
  .brand-mark__name {
    font-weight: 600; font-size: 13px; letter-spacing: 0.5px;
    color: var(--paper); line-height: 1;
  }
  .card--back .brand-mark { left: 227px; top: 86px; }
  .card--front .brand-mark { left: 393px; top: 80px; }

  .website {
    position: absolute; left: 164px; top: 253px; width: 222px; height: 76px;
    display: flex; align-items: center; justify-content: center; gap: 4px;
    color: var(--paper); font-size: 14.5px;
  }
  .website__icon { width: 12px; height: 12px; }

  .person { position: absolute; left: 51px; top: 58px; }
  .person__name {
    font-size: 19px; font-weight: 400; letter-spacing: 0.3px;
    color: var(--ink); text-transform: uppercase; line-height: 1.1;
  }
  .person__title { font-size: 14px; color: var(--ink); margin-left: 12px; margin-top: 2px; }

  .contact {
    position: absolute; left: 53px; display: flex; align-items: center; gap: 12px;
    font-size: 14.5px; color: var(--ink);
  }
  .contact--phone { top: 150px; }
  .contact--email { top: 198px; }
  .contact__icon { width: 19px; height: 19px; }

  .company {
    position: absolute; left: 57px; top: 241px; height: 44px;
    display: flex; align-items: center;
    color: var(--paper); font-size: 15px; font-weight: 600;
  }
</style>
</head>
<body>
<div class="sheet">

  <svg width="0" height="0" style="position:absolute" aria-hidden="true">
    <defs>
      <linearGradient id="tapestry" x1="0" y1="0" x2="1" y2="1">
        <stop offset="0" stop-color="#6a5830"/>
        <stop offset="0.5" stop-color="#7a6636"/>
        <stop offset="1" stop-color="#5e4e2b"/>
      </linearGradient>
    </defs>
  </svg>

  <!-- Back of card -->
  <section class="card card--back">
    <svg class="card__art" viewBox="0 0 550 329">
      <rect class="tapestry-fill" x="0" y="0" width="550" height="253" role="img" aria-label="Woven velvet tapestry lattice in gold and dark olive"/>
      <rect x="0" y="253" width="550" height="76" fill="var(--burgundy)"/>
      <rect x="164" y="253" width="222" height="76" fill="var(--gold)"/>
    </svg>
    <div class="brand-mark">
      <div class="brand-mark__square"></div>
      <span class="brand-mark__name">BROVENNA</span>
    </div>
    <div class="website">
      <svg class="website__icon" viewBox="0 0 12 12" aria-hidden="true">
        <circle cx="6" cy="6" r="5" fill="none" stroke="#fff" stroke-width="1.4"/>
        <path d="M1 6h10M6 1c-2.2 2.8-2.2 7.2 0 10M6 1c2.2 2.8 2.2 7.2 0 10" fill="none" stroke="#fff" stroke-width="1"/>
      </svg>
      <span>www.brovennatrading.example</span>
    </div>
  </section>

  <!-- Front of card -->
  <section class="card card--front">
    <svg class="card__art" viewBox="0 0 550 329">
      <polygon class="tapestry-fill" points="295,0 550,0 550,329 411,329" role="img" aria-label="Woven velvet tapestry lattice in gold and dark olive"/>
      <polygon points="250,0 310,0 326,46 268,56" fill="var(--burgundy)"/>
      <rect x="51" y="108" width="199" height="3" fill="var(--burgundy)"/>
      <polygon points="0,241 385,241 400,285 0,285" fill="var(--burgundy)"/>
      <polygon points="392,243 550,243 550,268 402,268" fill="var(--burgundy)"/>
    </svg>

    <div class="person">
      <h1 class="person__name">Marcus T. Hollenbrand</h1>
      <p class="person__title">C. E. O</p>
    </div>

    <div class="contact contact--phone">
      <svg class="contact__icon" viewBox="0 0 19 19" aria-hidden="true">
        <rect width="19" height="19" rx="2" fill="var(--burgundy)"/>
        <path d="M4 7c0-2 2-3 5.5-3S15 5 15 7l-2.2.6-.6-1.6H6.8l-.6 1.6z" fill="#fff"/>
        <rect x="5" y="9" width="9" height="6" rx="1" fill="#fff"/>
        <circle cx="9.5" cy="12" r="1.4" fill="var(--burgundy)"/>
      </svg>
      <span>555-294-6172</span>
    </div>

    <div class="contact contact--email">
      <svg class="contact__icon" viewBox="0 0 19 19" aria-hidden="true">
        <rect width="19" height="19" rx="2" fill="var(--burgundy)"/>
        <rect x="4" y="6" width="11" height="8" fill="none" stroke="#fff" stroke-width="1.3"/>
        <path d="M4 6l5.5 4.5L15 6" fill="none" stroke="#fff" stroke-width="1.3"/>
      </svg>
      <span>mark@brovennatrading.example</span>
    </div>

    <div class="company">Brovenna Trading/Shipping, LLC.</div>

    <div class="brand-mark">
      <div class="brand-mark__square"></div>
      <span class="brand-mark__name">BROVENNA</span>
    </div>
  </section>

</div>
</body>
</html>
```